Business card design for a dynamic IT consulting company

We need a business card design for a young firm, specialized in the Telecommunications/Consulting industry. The name of the company is Dulmar and Partners Business Consulting Ltd. (Short name: Dulmar and Partnes)
Dulmar = solve read reverse, so we aim to be uncomplicated and solution-oriented. The small pipe in our logo is also related to the word solve. So we need a new business card design, which is simple, eye catching and something non traditional (I would probably prefer a square shaped design rather than a rectangle, but open for suggestions). Attached our logo.

Target Market(s)

Usually our customers are Tier1 Telecoms providers (Q-Linkor, Teravine, etc) and their executives.

Industry/Entity Type

Business

Contact Information for Business Card

Name: Gergely Tarnavedi
Email: g.tarnavedi@dulmar-example.hu
Web: www.dulmar-example.hu
Mobile: +36 30 555 0192
Title: Managing Director

Optional:
Company name: Dulmar and Partners Ltd.
Address: 1021 Budapest, Kovarhegyi str. 17/B, Hungary

Font styles to use
Other font styles liked:
• helveticaneue_medium, Prime Regular are used now.

Colors

Designer to choose colors to be used in the design.

Requirements
Must have
• I would like to have a 2 sided design.
Nice to have
• I thought if we make the logo a bit bigger (without the company name), that could go to the back with the company name below. I though, if the pipe in the logo is somehow touchable on the business card, would be nice and unique.

```html
<!DOCTYPE html>
<html lang="en">
<head>
<meta charset="utf-8">
<title>Dulmar and Partners – Business Card</title>
<link rel="stylesheet" href="https://fonts.googleapis.com/css2?family=Arimo:wght@400;700&display=swap">
<style>
  :root {
    --page-bg: #e9e7e4;
    --card-front: #f7f7f7;
    --card-back: #1f2023;
    --band-grey: #6a6b6e;
    --accent-blue: #1a9ddb;
    --accent-magenta: #c2248f;
    --text-grey: #5a5b5e;
    --text-dark: #3c3d40;
    --text-light: #ffffff;
  }
  * { margin: 0; padding: 0; box-sizing: border-box; }
  html, body { width: 1200px; height: 960px; overflow: hidden; }
  body {
    background: var(--page-bg);
    font-family: "Arimo", Arial, sans-serif;
    position: relative;
  }
  .card {
    position: absolute;
    top: 305px;
    width: 343px;
    height: 343px;
    overflow: hidden;
    box-shadow: 0 2px 6px rgba(0,0,0,0.25);
  }
  .card--front { left: 200px; background: var(--card-front); }
  .card--back { left: 652px; background: var(--card-back); }

  .front-curves { position: absolute; inset: 0; }

  .brand {
    position: absolute;
    top: 44px;
    left: 40px;
    display: flex;
    align-items: center;
    gap: 8px;
  }
  .brand__square {
    width: 16px; height: 16px;
    background: var(--accent-blue);
  }
  .brand__name {
    font-size: 27px;
    font-weight: 400;
    color: var(--text-dark);
    letter-spacing: -0.3px;
  }

  .contact {
    position: absolute;
    right: 38px;
    top: 130px;
    text-align: right;
  }
  .contact__name {
    font-size: 19px;
    font-weight: 700;
    color: var(--accent-blue);
    letter-spacing: 0.3px;
  }
  .contact__title {
    font-size: 14.5px;
    color: var(--text-grey);
    letter-spacing: 0.4px;
    margin-top: 2px;
  }
  .contact__address {
    margin-top: 16px;
    font-size: 13.5px;
    line-height: 19px;
    color: var(--text-grey);
  }
  .contact__lines {
    position: absolute;
    right: 38px;
    top: 252px;
    font-size: 13.5px;
    line-height: 19px;
    color: var(--text-grey);
    text-align: right;
  }
  .contact__line { display: flex; justify-content: flex-end; align-items: center; gap: 8px; }
  .contact__icon { width: 11px; height: 12px; flex: none; }

  .back-pattern {
    position: absolute;
    inset: 0;
    background: radial-gradient(circle at 60% 40%, #2a2b31 0%, #1f2023 70%);
  }
  .back-brand {
    position: absolute;
    right: 33px;
    top: 258px;
    display: flex;
    align-items: center;
    gap: 7px;
  }
  .back-brand__square { width: 11px; height: 11px; background: var(--accent-magenta); }
  .back-brand__name { font-size: 16px; color: var(--text-light); }
  .back-url {
    position: absolute;
    right: 33px;
    top: 297px;
    font-size: 13.5px;
    color: var(--text-light);
  }
</style>
</head>
<body>
  <section class="card card--front" aria-label="Card front">
    <svg class="front-curves" width="343" height="343" viewBox="0 0 343 343" aria-hidden="true">
      <path d="M0 0 H10 C10 120 28 250 72 343 H0 Z" fill="var(--band-grey)"/>
      <path d="M15 0 C15 120 36 250 84 343" fill="none" stroke="var(--accent-blue)" stroke-width="6"/>
    </svg>

    <div class="brand">
      <span class="brand__square"></span>
      <span class="brand__name">Dulmar &amp; Partners</span>
    </div>

    <div class="contact">
      <p class="contact__name">GERGELY TARNAVEDI</p>
      <p class="contact__title">MANAGING DIRECTOR</p>
      <p class="contact__address">
        Dulmar and Partners Ltd.<br>
        1021 Budapest<br>
        Kovarhegyi str. 17/B, Hungary
      </p>
    </div>

    <div class="contact__lines">
      <p class="contact__line">+36 30 555 0192
        <svg class="contact__icon" viewBox="0 0 11 12" aria-hidden="true"><rect x="2" y="0.5" width="7" height="11" rx="1.2" fill="none" stroke="var(--accent-blue)" stroke-width="1.2"/><rect x="4.5" y="9.2" width="2" height="1" fill="var(--accent-blue)"/></svg>
      </p>
      <p class="contact__line">g.tarnavedi@dulmar-example.hu
        <svg class="contact__icon" viewBox="0 0 11 12" aria-hidden="true"><rect x="0.5" y="3" width="10" height="7" fill="var(--accent-blue)"/><path d="M0.5 3 L5.5 7 L10.5 3" fill="none" stroke="#fff" stroke-width="1"/></svg>
      </p>
    </div>
  </section>

  <section class="card card--back" aria-label="Card back">
    <div class="back-pattern" role="img" aria-label="Faint grid of small coloured squares across the dark background"></div>
    <div class="back-brand">
      <span class="back-brand__square"></span>
      <span class="back-brand__name">Dulmar &amp; Partners</span>
    </div>
    <p class="back-url">www.dulmar-example.hu</p>
  </section>
</body>
</html>
```